Online Prescription Eyeglass Lens Company Needs a Website

*Update new name to ClearPair. Thx

We are eye doctors with a lab that need a website for a new company based in Southern California called ClearPair. We replace old prescription lenses with new ones next day for most lenses. Patients select the lenses and give us the prescription. We then send a box with a prepaid shipping label. Place the frames in the box and drop them in the mail to our lab. We will custom make new lenses, fit them back into your frames and send them back to you. We would like to compete with www.vizora.com and offer affordable lenses for single vision, bifocal, progressive, sunglass lenses at an affordable price with next day shipping.
Updates

Hi Designers, We have a new name called ClearPair. Can we have the website design reflect the new name and we'll pick our favorites. Thx

Update: The new name is OptiNova . I have not made very many changes or feedback to the submissions because we were bidding for a .com. We won and our new name is OptiNova . This is the last name change.. Please have the website reflect the new name and I'll be providing feedback on the websites . ( I have a separate project for the logo people are working on, so don't worry about creating a logo). Look forward to the submissions. Thanks everyone.

Hi, Just leave the name as ClearPair for now. I will narrow down top designs tonight. Thx

Target Market(s)

Anyone that wears prescription or nonprescription glasses or sunglasses that want next day shipping.

Industry/Entity Type

Eyewear

Number of Pages Required

4 page

Font styles to use
Serif

Colors

Designer to choose colors to be used in the design.

Requirements
Must have
• I need a website that can compete with https://www.vizora.com/.
• We are different from vizora because we can offer same day service or next day shipping.
• It needs to have website that offers the lenses available listed below.
• Needs to be able to upload a prescription and payment feature.
• Pictures of different types of options with small info about each lens option.
• Template Pricing (just use numbers from $79-$179 for now)
• SINGLE VISION LENSES
• HIGH INDEX LENSES
• READING LENSES
• DIGITAL HD PROGRESSIVE LENSES
• RX & NON-RX SUNGLASSES
• RX & NON-RX POLARIZED SUNGLASSES
• COMPUTER LENSES
• TRANSITION LENSES
• BI-FOCAL LENSES

```html
<!DOCTYPE html>
<html lang="en">
<head>
<meta charset="utf-8">
<title>ClearPair — Prescription Lenses</title>
<link rel="stylesheet" href="https://fonts.googleapis.com/css2?family=Poppins:wght@400;500;600&family=Roboto:ital,wght@0,400;0,500;0,700;1,400&display=swap">
<style>
:root{
  --blue:#0f9ee0;
  --blue-dark:#0a8bc8;
  --hero-a:#2eaed6;
  --hero-b:#79d3ea;
  --green:#8cc63f;
  --ink:#222;
  --muted:#666;
  --grey-bg:#e6e6e6;
  --light-bg:#f1f1f1;
  --dark:#2d2e38;
  --white:#fff;
}
*{box-sizing:border-box;margin:0;padding:0}
html,body{width:1200px;height:3789px;overflow:hidden}
body{font-family:'Roboto',sans-serif;color:var(--ink);background:var(--white);position:relative}
.abs{position:absolute}
h1,h2,h3,.logo-name{font-family:'Poppins',sans-serif;font-weight:400}
.btn{position:absolute;display:flex;align-items:center;justify-content:center;gap:10px;font-family:'Roboto',sans-serif;font-weight:700;font-size:12px;letter-spacing:.3px;text-transform:uppercase;color:var(--white);background:var(--blue);text-decoration:none}
.btn .arrow{font-size:15px;font-weight:400}

/* header */
.site-header{position:absolute;top:0;left:0;width:1200px;height:68px;background:var(--white)}
.logo{position:absolute;display:flex;align-items:center;gap:10px}
.logo-dot{width:30px;height:30px;border-radius:50%;background:var(--blue)}
.logo-name{font-size:22px;font-weight:500;color:var(--ink)}
.main-nav a{position:absolute;top:27px;font-size:12px;font-weight:500;color:var(--ink);text-decoration:none;text-transform:uppercase}
.nav-order{position:absolute;left:1030px;top:0;width:170px;height:68px;background:#f4f4f4;color:var(--green);font-size:12px;font-weight:700;display:flex;align-items:center;justify-content:center;text-decoration:none}

/* hero */
.hero{position:absolute;top:68px;left:0;width:1200px;height:609px;background:linear-gradient(100deg,var(--hero-a),var(--hero-b) 70%,#a9e2f0)}
.hero-photo{position:absolute;left:690px;top:0;width:380px;height:609px;background:radial-gradient(ellipse at 50% 40%,#f0b24a 0%,#e9a23a 40%,rgba(233,162,58,0) 72%)}
.hero h1{position:absolute;left:88px;top:228px;font-size:46px;font-weight:500;color:var(--white)}
.hero .lead{position:absolute;left:88px;top:300px;font-size:17px;font-weight:700;color:var(--white)}
.hero .price{position:absolute;left:88px;top:325px;font-size:21px;font-weight:700;color:var(--white)}
.hero .btn-choose{left:88px;top:384px;width:220px;height:46px;background:var(--green)}
.hero .btn-how{left:321px;top:384px;width:192px;height:46px;background:transparent;border:1.5px solid var(--white)}
.dots{position:absolute;display:flex;gap:8px}
.dots span{width:9px;height:9px;border-radius:50%;border:1.5px solid rgba(255,255,255,.8)}
.dots span.on{background:var(--white)}

/* sections */
.section-title{position:absolute;left:0;width:1200px;text-align:center;font-size:30px;color:var(--ink)}
.section-sub{position:absolute;left:400px;width:400px;text-align:center;font-size:13px;line-height:21px;color:var(--muted)}

.how{position:absolute;top:677px;left:0;width:1200px;height:669px;background:var(--white)}
.step-line{position:absolute;left:217px;top:321px;width:773px;height:3px;background:var(--blue)}
.step-art{position:absolute;width:130px;height:130px;top:258px;border-radius:50%;background:radial-gradient(circle,#d6effb 0%,#e9f6fd 60%,rgba(255,255,255,0) 72%)}
.step-label{position:absolute;top:410px;width:220px;text-align:center;font-size:15px;font-weight:500;color:var(--ink)}
.how .btn{left:498px;top:503px;width:202px;height:53px}

.lab{position:absolute;top:1346px;left:0;width:1200px;height:574px;background:var(--grey-bg)}
.lab h2{position:absolute;left:88px;top:196px;font-size:32px}
.lab p{position:absolute;left:88px;top:258px;width:470px;font-size:13px;line-height:21px;color:#555}
.lab .btn{left:88px;top:354px;width:228px;height:58px}
.lab-photo{position:absolute;left:599px;top:86px;width:512px;height:402px;background:linear-gradient(135deg,#cfd6dc,#eef1f3 45%,#a9b3bc);box-shadow:0 14px 30px rgba(0,0,0,.22)}

.lenses{position:absolute;top:1920px;left:0;width:1200px;height:624px;background:var(--white)}
.lens-card{position:absolute;top:206px;width:340px;text-align:center}
.lens-card h3{font-family:'Poppins',sans-serif;font-size:15px;font-weight:500;color:var(--ink)}
.lens-art{width:180px;height:70px;margin:22px auto 14px;border-radius:35px;background:linear-gradient(90deg,#e4e4e4,#f5f5f5,#e4e4e4)}
.lens-card p{font-size:12px;line-height:20px;color:#555;width:280px;margin:0 auto}
.lens-card .cost{font-size:18px;font-weight:700;color:var(--blue);margin-top:8px}
.lenses .btn{left:488px;top:452px;width:224px;height:53px}

.join{position:absolute;top:2544px;left:0;width:1200px;height:222px;background:var(--dark)}
.join-art{position:absolute;left:88px;top:70px;width:139px;height:84px;border-radius:42px;background:#45475a}
.join h2{position:absolute;left:245px;top:76px;font-size:30px;color:var(--white)}
.join p{position:absolute;left:245px;top:126px;font-size:14px;line-height:22px;color:#d4d4d8}
.join-field{position:absolute;left:690px;top:93px;width:358px;height:56px;background:var(--white);display:flex;align-items:center;gap:10px;padding-left:22px;font-size:12px;color:#999}
.join-send{position:absolute;left:1048px;top:93px;width:63px;height:56px;background:var(--green);display:flex;align-items:center;justify-content:center}

.reviews{position:absolute;top:2766px;left:0;width:1200px;height:513px;background:var(--white);overflow:hidden}
.avatar{position:absolute;border-radius:50%;background:linear-gradient(135deg,#c9ced4,#9aa3ad)}
.quote-mark{position:absolute;left:0;width:1200px;top:220px;text-align:center;font-family:'Poppins',sans-serif;font-size:60px;font-weight:600;color:var(--green);line-height:60px}
.quote-text{position:absolute;left:300px;width:600px;top:285px;text-align:center;font-size:13px;font-style:italic;line-height:24px;color:#666}
.quote-name{position:absolute;left:0;width:1200px;top:350px;text-align:center;font-size:14px;font-weight:500}
.reviews .dots span{border-color:#6ec4ec}
.reviews .dots span.on{background:var(--blue);border-color:var(--blue)}

.footer{position:absolute;top:3279px;left:0;width:1200px;height:465px;background:var(--light-bg)}
.cta-text{position:absolute;left:341px;top:66px;font-family:'Poppins',sans-serif;font-size:26px;font-weight:500}
.footer .btn{left:634px;top:55px;width:222px;height:53px}
.social{position:absolute;left:119px;top:336px;display:flex;gap:11px}
.social span{width:34px;height:34px;border-radius:50%}
.col-title{position:absolute;top:228px;font-family:'Poppins',sans-serif;font-size:15px;font-weight:500}
.links a{position:absolute;left:394px;font-size:12px;color:#444;text-decoration:none}
.news-date{position:absolute;left:604px;font-size:10px;color:#777}
.news-title{position:absolute;left:604px;font-size:14px;color:var(--ink)}
.sub-text{position:absolute;left:879px;top:273px;font-size:12px;line-height:22px;color:#444}
.sub-field{position:absolute;left:879px;top:328px;width:232px;height:43px;background:var(--white);display:flex;align-items:center;gap:8px;padding-left:14px;font-size:12px;color:#999}
.sub-send{position:absolute;left:1081px;top:340px}

.copyright{position:absolute;top:3744px;left:0;width:1200px;height:45px;background:var(--white);text-align:center;line-height:45px;font-size:12px;color:#444}
.to-top{position:absolute;left:1137px;top:3721px;width:40px;height:40px;border-radius:50%;background:var(--green);display:flex;align-items:center;justify-content:center}
</style>
</head>
<body>

<header class="site-header">
  <div class="logo" style="left:88px;top:19px"><span class="logo-dot"></span><span class="logo-name">ClearPair</span></div>
  <nav class="main-nav">
    <a href="#" style="left:467px">Our Lenses</a>
    <a href="#" style="left:586px">Why Vizora</a>
    <a href="#" style="left:715px">The Lab</a>
    <a href="#" style="left:808px">Our Process</a>
    <a href="#" style="left:955px">Sign In</a>
  </nav>
  <a class="nav-order" href="#">ORDER LENSES</a>
</header>

<section class="hero">
  <div class="hero-photo" role="img" aria-label="Smiling woman in a sun hat, sunglasses and a yellow sweater"></div>
  <h1>Contact Lenses</h1>
  <p class="lead">Let us help you discover the freedom and benefits of</p>
  <p class="price">Starting at $79</p>
  <a class="btn btn-choose" href="#">Choose your lenses <span class="arrow">→</span></a>
  <a class="btn btn-how" href="#">See how it's done <span class="arrow">→</span></a>
  <div class="dots" style="left:583px;top:552px"><span></span><span class="on"></span><span></span></div>
</section>

<section class="how">
  <h2 class="section-title" style="top:116px">How ClearPair Works</h2>
  <p class="section-sub" style="top:172px">Lorem ipsum dolor sit amet, consectetuer adipiscing elit aenean commodo ligula eget dolor.</p>
  <div class="step-line"></div>
  <div class="step-art" style="left:152px" role="img" aria-label="Person choosing lenses at a computer"></div>
  <div class="step-art" style="left:402px" role="img" aria-label="Mailbox with frames being sent"></div>
  <div class="step-art" style="left:693px" role="img" aria-label="Lab technician fitting new lenses"></div>
  <div class="step-art" style="left:925px" role="img" aria-label="Happy customer wearing finished glasses"></div>
  <p class="step-label" style="left:107px">Pick Your Lenses</p>
  <p class="step-label" style="left:357px">Send Us Your Frames</p>
  <p class="step-label" style="left:648px">We Re Lens Your Glasses</p>
  <p class="step-label" style="left:880px">Sight, sealed, delivered</p>
  <a class="btn" href="#">Refer and earn <span class="arrow">→</span></a>
</section>

<section class="lab">
  <h2>Our Lab, Our Quality</h2>
  <p>Aenean commodo ligula eget dolor. Aenean massa. Cum sociis natoque penatibus et magnis dis parturient montes, nascetur ridiculus mus. Donec quam felis, ultricies nec, pellentesque eu, pretium quis</p>
  <a class="btn" href="#">Learn more about us <span class="arrow">→</span></a>
  <div class="lab-photo" role="img" aria-label="Lab technician examining a sample under a microscope"></div>
</section>

<section class="lenses">
  <h2 class="section-title" style="top:124px">Our Lenses</h2>
  <div class="lens-card" style="left:90px">
    <h3>Single Vision Lenses</h3>
    <div class="lens-art" role="img" aria-label="Round dark eyeglass frames"></div>
    <p>Lorem ipsum dolor sit amet, consectetuer adipis cing elit. Aenean commodo ligula</p>
    <p class="cost">$79.00</p>
  </div>
  <div class="lens-card" style="left:429px">
    <h3>High Index Lenses</h3>
    <div class="lens-art" role="img" aria-label="Tortoiseshell eyeglass frames"></div>
    <p>Lorem ipsum dolor sit amet, consectetuer adipis cing elit. Aenean commodo ligula</p>
    <p class="cost">$100.00</p>
  </div>
  <div class="lens-card" style="left:770px">
    <h3>Reading Lenses</h3>
    <div class="lens-art" role="img" aria-label="Black rectangular reading glasses"></div>
    <p>Lorem ipsum dolor sit amet, consectetuer adipis cing elit. Aenean commodo ligula</p>
    <p class="cost">$160.00</p>
  </div>
  <a class="btn" href="#">View more lenses <span class="arrow">→</span></a>
</section>

<section class="join">
  <div class="join-art" role="img" aria-label="Cartoon glasses with eyes"></div>
  <h2>Join the Family</h2>
  <p>Subscribe to stay up to date with weekly specials<br>and subscriber exclusives.</p>
  <div class="join-field">
    <svg width="13" height="10" viewBox="0 0 13 10"><rect x=".5" y=".5" width="12" height="9" fill="#bbb"/><path d="M.5 .5 6.5 5.5 12.5 .5" stroke="#fff" fill="none"/></svg>
    Enter your email address
  </div>
  <div class="join-send">
    <svg width="18" height="18" viewBox="0 0 18 18"><path d="M1 8 17 1 11 17 8 10Z" fill="#fff"/></svg>
  </div>
</section>

<section class="reviews">
  <div class="avatar" role="img" aria-label="Customer portrait" style="left:101px;top:101px;width:40px;height:40px"></div>
  <div class="avatar" role="img" aria-label="Customer portrait" style="left:-17px;top:176px;width:60px;height:60px"></div>
  <div class="avatar" role="img" aria-label="Customer portrait" style="left:83px;top:200px;width:36px;height:36px"></div>
  <div class="avatar" role="img" aria-label="Customer portrait" style="left:149px;top:244px;width:46px;height:46px"></div>
  <div class="avatar" role="img" aria-label="Customer portrait" style="left:38px;top:297px;width:26px;height:26px"></div>
  <div class="avatar" role="img" aria-label="Customer portrait" style="left:73px;top:340px;width:56px;height:56px"></div>
  <div class="avatar" role="img" aria-label="Customer portrait" style="left:1154px;top:112px;width:26px;height:26px"></div>
  <div class="avatar" role="img" aria-label="Customer portrait" style="left:1154px;top:200px;width:66px;height:66px"></div>
  <div class="avatar" role="img" aria-label="Customer portrait" style="left:1081px;top:212px;width:40px;height:40px"></div>
  <div class="avatar" role="img" aria-label="Customer portrait" style="left:988px;top:168px;width:36px;height:36px"></div>
  <div class="avatar" role="img" aria-label="Customer portrait" style="left:1006px;top:297px;width:50px;height:50px"></div>
  <div class="avatar" role="img" aria-label="Customer portrait" style="left:1124px;top:305px;width:36px;height:36px"></div>
  <h2 class="section-title" style="top:172px">Clients Review</h2>
  <div class="quote-mark">“</div>
  <p class="quote-text">"Donec leo ligula porttitor eu consequat vitae eleifend ac enim. Aliquam lorem ante dapibus in viverra quis feugiat a tellus phasellus viverra nulla ut metus varius"</p>
  <p class="quote-name">~John Doe</p>
  <div class="dots" style="left:575px;top:402px"><span class="on"></span><span></span><span></span></div>
</section>

<footer class="footer">
  <p class="cta-text">Like what you see ?</p>
  <a class="btn" href="#">Let's get you started <span class="arrow">→</span></a>

  <div class="logo" style="left:119px;top:275px"><span class="logo-dot"></span><span class="logo-name">ClearPair</span></div>
  <div class="social">
    <span style="background:#3b5998"></span><span style="background:#1da1f2"></span><span style="background:#d93a2b"></span><span style="background:#0e76a8"></span>
  </div>

  <h3 class="col-title" style="left:394px">Quick Links</h3>
  <nav class="links">
    <a href="#" style="top:275px">Our lenses</a>
    <a href="#" style="top:305px">Why vizora</a>
    <a href="#" style="top:338px">The lab</a>
    <a href="#" style="top:371px">Our process</a>
  </nav>

  <h3 class="col-title" style="left:604px">Latest News</h3>
  <p class="news-date" style="top:273px">4th October 2017</p>
  <p class="news-title" style="top:294px">News title goes here..</p>
  <p class="news-date" style="top:336px">7th October 2017</p>
  <p class="news-title" style="top:357px">Latest news goes here..</p>

  <h3 class="col-title" style="left:879px">Subscribe</h3>
  <p class="sub-text">Subscribe to our email newsletter<br>to get latest new and updates</p>
  <div class="sub-field">
    <svg width="12" height="9" viewBox="0 0 12 9"><rect x=".5" y=".5" width="11" height="8" fill="#bbb"/><path d="M.5 .5 6 5 11.5 .5" stroke="#fff" fill="none"/></svg>
    Email address
  </div>
  <svg class="sub-send" width="18" height="18" viewBox="0 0 18 18"><path d="M1 8 17 1 11 17 8 10Z" fill="var(--blue)"/></svg>
</footer>

<div class="copyright">© 2017, All Rights Reserved</div>
<div class="to-top">
  <svg width="14" height="10" viewBox="0 0 14 10"><path d="M1 9 7 2 13 9" stroke="#fff" stroke-width="2" fill="none"/></svg>
</div>

</body>
</html>
```